Creation of a construction/bricklaying business website

Following the template format of "Kestrow 2", the following content would need to be included:
1. Landing page with 3 tiles that go to their own pages.
- Landing page to include background photo and description of services offered.
2. 3 tiles to include:
a) "Contact Us For A Free Quote or Friendly Discussion" Form (middle tile)
b) Case Studies and Testimonials
c) Certifications and Professional Membership
- Design logo to be used from previous ArtQuorum project. Example of logo attached below, please access full JPG files from our account.

Target Market(s)

Prospective clients seeking construction work (bricklaying speciality)

Industry/Entity Type

Residential Construction

Coding

Coded - Design and coding required

Number of Pages Required

4 page

Font styles to use
Sans Serif

Colors

Designer to choose colors to be used in the design.

Requirements
Must have
• Following the template format of "Kestrow 2", the following content would need to be included:
• 1. Landing parent page with 3 tiles that go to the 3 child pages.
• - Landing page to include background photo and description of services offered.
• 2. 3 tiles to include:
• a) "Contact Us For A Free Quote or Friendly Discussion" Form (middle tile)
• b) Case Studies and Testimonials (first tile / left side)
• c) Certifications and Professional Memberships (third tile / right side) (This should include logos of the relevant organisations being displayed. Specifically GLW and the Keel Gate GLW).
• - Design logo to be used from previous ArtQuorum project. Example of logo attached below, please access full JPG files from our account.
Nice to have
• Sleek and modern feel.
• Approachable in terms of how people can contact the company for a quote.
• Traditional pictures to give credibility and comfort around choosing this company.
Should not have
• Cheesy pictures
• Over-complicated
• Simple to use
• Easy URL domain name

```html
<!DOCTYPE html>
<html lang="en">
<head>
<meta charset="utf-8">
<title>R.T.Harlow Construction Ltd</title>
<link rel="stylesheet" href="https://fonts.googleapis.com/css2?family=Oswald:wght@400;500&family=Montserrat:wght@400;500;600&family=Raleway:wght@400;500&display=swap">
<style>
:root{
  --blue:#0f4fa8;
  --blue-dark:#0b3f8a;
  --ink:#333;
  --muted:#666;
  --page:#f2f2f2;
  --panel:#ffffff;
  --line:#dcdcdc;
  --button:#5a5a5a;
  --footer:#262626;
  --footer-bar:#1c1c1c;
  --footer-text:#e8e8e8;
  --badge-red:#b5123e;
  --badge-orange:#e0421b;
}
*{box-sizing:border-box;margin:0;padding:0}
html,body{width:1025px;height:1200px;overflow:hidden}
body{background:var(--page);font-family:'Raleway',sans-serif;color:var(--ink);position:relative}

.site-header{position:absolute;left:0;top:0;width:1025px;height:94px;background:#fff;border-top:2px solid var(--blue)}
.contact-tab{position:absolute;left:596px;top:0;width:324px;height:31px;background:var(--blue);border-radius:0 0 14px 14px;display:flex;align-items:center;justify-content:center;gap:22px;color:#fff;font-family:'Montserrat',sans-serif;font-size:12px}
.contact-tab span{display:flex;align-items:center;gap:6px}
.contact-tab .sep{width:1px;height:18px;background:rgba(255,255,255,.4)}
.brand{position:absolute;left:96px;top:28px;font-family:'Montserrat',sans-serif;font-weight:600;font-size:21px;color:var(--blue);display:flex;align-items:center;gap:8px}
.brand .mark{width:12px;height:12px;background:var(--blue)}
.main-nav{position:absolute;top:56px;left:402px;display:flex;font-family:'Montserrat',sans-serif;font-size:11.5px;color:#666}
.main-nav a{color:inherit;text-decoration:none;padding:0 18px;border-left:1px solid #ddd;line-height:14px}
.main-nav a:first-child{padding-left:0;border-left:none;color:var(--blue);font-weight:500;position:relative}
.main-nav a:first-child::after{content:"";position:absolute;left:0;right:18px;bottom:-9px;height:2px;background:var(--blue)}

.hero{position:absolute;left:0;top:94px;width:1025px;height:496px}
.hero-photo{position:absolute;inset:0;background:linear-gradient(115deg,#8a8585 0%,#9c6b5c 30%,#b86a52 55%,#a95f4c 80%,#8e5a4d 100%)}
.hero-title{position:absolute;left:0;right:0;top:130px;text-align:center;font-family:'Oswald',sans-serif;font-weight:400;font-size:34px;line-height:39px;color:#fff;text-shadow:0 2px 6px rgba(0,0,0,.35)}
.service{position:absolute;display:flex;align-items:center;gap:12px;font-family:'Montserrat',sans-serif;font-size:22px;color:#fff;text-shadow:0 2px 5px rgba(0,0,0,.35)}
.service .icon{width:46px;height:46px;background:#fff;border-radius:6px;display:flex;align-items:center;justify-content:center;box-shadow:0 1px 3px rgba(0,0,0,.3)}

.tile{position:absolute;top:653px;width:262px;height:317px;background:var(--panel);border:1px solid #e6e6e6}
.tile-head{height:38px;background:var(--blue);color:#fff;font-family:'Montserrat',sans-serif;font-weight:500;font-size:14px;display:flex;align-items:center;justify-content:center;letter-spacing:.2px}
.tile-btn{position:absolute;bottom:-16px;left:50%;transform:translateX(-50%);width:107px;height:30px;background:var(--button);color:#fff;font-family:'Montserrat',sans-serif;font-size:14px;font-weight:500;display:flex;align-items:center;justify-content:center;letter-spacing:.5px}
.testimonial{padding:13px 15px 0 16px;font-size:12px;line-height:20.8px;text-align:justify;color:#555;position:relative}
.testimonial .quote-mark{position:absolute;left:10px;top:-2px;font-family:'Oswald',sans-serif;font-size:80px;color:#e8e8e8;line-height:1}
.testimonial p{position:relative}
.testimonial .author{text-align:right;font-family:'Montserrat',sans-serif;font-size:13px;color:#444;margin-top:4px;line-height:16px}
.testimonial .place{text-align:right;font-size:12px;color:#666;line-height:16px}

.form{padding:12px 19px 0 19px;display:grid;grid-template-columns:1fr 1fr;column-gap:7px}
.field{display:flex;flex-direction:column;margin-bottom:8px}
.field.wide{grid-column:1/3}
.field label{font-size:9.5px;color:#666;margin-bottom:4px;font-family:'Montserrat',sans-serif}
.field .input{height:30px;border:1px solid var(--line);background:#fff}
.field .input.tall{height:49px}

.badges{display:flex;flex-direction:column;align-items:center;padding-top:15px}
.badge-glw{width:82px;height:136px;background:var(--badge-red);border-radius:3px}
.badge-divider{width:236px;border-top:1px dashed var(--line);margin:18px 0}
.badge-keel{width:142px;height:72px;background:#fff;border:2px solid var(--badge-orange);border-radius:3px;display:flex;align-items:flex-end}
.badge-keel span{display:block;width:100%;height:12px;background:var(--badge-orange)}

.site-footer{position:absolute;left:0;top:1050px;width:1025px;height:112px;background:var(--footer);color:var(--footer-text);border-top:1px solid var(--blue)}
.foot-address{position:absolute;left:98px;top:28px;display:flex;gap:12px}
.foot-address .name{font-family:'Montserrat',sans-serif;font-size:12px}
.foot-address .lines{font-family:'Montserrat',sans-serif;font-size:10px;line-height:14.5px;margin-top:2px}
.foot-divider{position:absolute;top:28px;width:1px;height:58px;background:#555}
.foot-contact{position:absolute;left:436px;font-family:'Montserrat',sans-serif;font-size:12px;display:flex;align-items:center;gap:14px}
.foot-brand{position:absolute;left:740px;top:46px;font-family:'Montserrat',sans-serif;font-weight:600;font-size:20px;color:#bdbdbd;display:flex;align-items:center;gap:8px}
.foot-brand .mark{width:12px;height:12px;background:#bdbdbd}
.foot-bar{position:absolute;left:0;top:1162px;width:1025px;height:38px;background:var(--footer-bar);color:#bbb;font-family:'Montserrat',sans-serif;font-size:10.5px}
.foot-bar .copy{position:absolute;left:97px;top:13px}
.social{position:absolute;right:98px;top:5px;display:flex;gap:13px}
.social span{width:27px;height:27px;border-radius:50%;background:#1f5fb3;border:2px solid #ddd}
</style>
</head>
<body>

<header class="site-header">
  <div class="contact-tab">
    <span><svg width="13" height="10" viewBox="0 0 13 10"><rect x="0.5" y="0.5" width="12" height="9" fill="none" stroke="#fff"/><path d="M0.5 0.5 6.5 5.5 12.5 0.5" fill="none" stroke="#fff"/></svg>info@rtharlow.com</span>
    <i class="sep"></i>
    <span style="font-weight:600"><svg width="12" height="12" viewBox="0 0 24 24"><path fill="#fff" d="M6.6 10.8a15 15 0 0 0 6.6 6.6l2.2-2.2a1 1 0 0 1 1-.25 11.4 11.4 0 0 0 3.6.57 1 1 0 0 1 1 1V20a1 1 0 0 1-1 1A17 17 0 0 1 3 4a1 1 0 0 1 1-1h3.5a1 1 0 0 1 1 1c0 1.25.2 2.450.57 3.57a1 1 0 0 1-.25 1z"/></svg>07700900417</span>
  </div>
  <div class="brand"><i class="mark"></i>R.T.Harlow Construction Ltd</div>
  <nav class="main-nav">
    <a href="#">Home</a><a href="#">Services</a><a href="#">Testimonials</a><a href="#">Case Studies</a><a href="#">Membership</a><a href="#">Contact</a>
  </nav>
</header>

<section class="hero">
  <div class="hero-photo" role="img" aria-label="Close-up photograph of a black wall lantern on red brickwork beneath a tiled roof edge"></div>
  <h1 class="hero-title">R.T.Harlow Construction Ltd is a construction company that<br>has expertise and experience in the following areas:</h1>

  <div class="service" style="left:154px;top:253px"><span class="icon"><svg width="30" height="26" viewBox="0 0 30 26"><path d="M2 12 15 2 28 12" fill="none" stroke="#0f4fa8" stroke-width="3"/><rect x="6" y="12" width="18" height="12" fill="#0f4fa8"/></svg></span>Extensions</div>
  <div class="service" style="left:421px;top:253px"><span class="icon"><svg width="30" height="24" viewBox="0 0 30 24" fill="#0f4fa8"><rect x="2" y="2" width="12" height="5"/><rect x="16" y="2" width="12" height="5"/><rect x="8" y="9" width="14" height="5"/><rect x="2" y="16" width="12" height="5"/><rect x="16" y="16" width="12" height="5"/></svg></span>Brickwork</div>
  <div class="service" style="left:669px;top:253px"><span class="icon"><svg width="28" height="28" viewBox="0 0 28 28"><rect x="2" y="2" width="24" height="24" fill="none" stroke="#0f4fa8" stroke-width="3"/><path d="M6 6 22 22H6z" fill="#0f4fa8"/></svg></span>Plastering</div>
  <div class="service" style="left:154px;top:320px"><span class="icon"><svg width="28" height="26" viewBox="0 0 28 26" fill="#0f4fa8"><rect x="3" y="3" width="4" height="21"/><rect x="12" y="3" width="4" height="21"/><rect x="21" y="3" width="4" height="21"/><rect x="1" y="9" width="26" height="3"/><rect x="1" y="17" width="26" height="3"/></svg></span>Garden walls</div>
  <div class="service" style="left:421px;top:318px"><span class="icon"><svg width="30" height="26" viewBox="0 0 30 26"><path d="M3 12 15 3 27 12" fill="none" stroke="#0f4fa8" stroke-width="3"/><rect x="7" y="12" width="16" height="11" fill="#0f4fa8"/><rect x="13" y="16" width="4" height="7" fill="#fff"/></svg></span>New houses</div>
  <div class="service" style="left:669px;top:320px"><span class="icon"><svg width="28" height="26" viewBox="0 0 28 26" fill="#0f4fa8"><rect x="2" y="20" width="24" height="4"/><path d="M4 18 14 8l4 4-8 6z"/><rect x="16" y="4" width="8" height="6"/></svg></span>Groundworks</div>
</section>

<section class="tile" style="left:96px">
  <h2 class="tile-head">CASE STUDIES &amp; TESTIMONIALS</h2>
  <div class="testimonial">
    <span class="quote-mark">&ldquo;</span>
    <p>I asked R.T.Harlow Construction Ltd to build a wall between the public footpath and my property. This job consisted of using old London stock brick and coping stones on top of the wall. The finished product was very good and blended in with the old type of brickwork in the area. I would strongly recommend this company.</p>
    <p class="author">- Margaret</p>
    <p class="place">(London)</p>
  </div>
  <a class="tile-btn">VIEW ALL</a>
</section>

<section class="tile" style="left:381px">
  <h2 class="tile-head">FRIENDLY DISCUSSION</h2>
  <div class="form">
    <div class="field"><label>First Name *</label><div class="input"></div></div>
    <div class="field"><label>Last Name *</label><div class="input"></div></div>
    <div class="field wide"><label>Email *</label><div class="input"></div></div>
    <div class="field"><label>Phone *</label><div class="input"></div></div>
    <div class="field"><label>Pincode *</label><div class="input"></div></div>
    <div class="field wide"><label>Description *</label><div class="input tall"></div></div>
  </div>
  <a class="tile-btn">SUBMIT</a>
</section>

<section class="tile" style="left:666px">
  <h2 class="tile-head">CERTIFICATIONS &amp; MEMBERSHIP</h2>
  <div class="badges">
    <div class="badge-glw" role="img" aria-label="GLW membership badge"></div>
    <div class="badge-divider"></div>
    <div class="badge-keel" role="img" aria-label="Keel Gate GLW certification badge"><span></span></div>
  </div>
</section>

<footer class="site-footer">
  <div class="foot-address">
    <svg width="18" height="22" viewBox="0 0 18 22"><path d="M9 0a8 8 0 0 0-8 8c0 6 8 14 8 14s8-8 8-14a8 8 0 0 0-8-8z" fill="#fff"/><circle cx="9" cy="8" r="3" fill="#262626"/></svg>
    <div>
      <div class="name">RTHarlow Construction LTD.</div>
      <div class="lines">14 Alder Lane,<br>Brookfield, London,<br>United Kingdom. N4 8QT</div>
    </div>
  </div>
  <div class="foot-divider" style="left:360px"></div>
  <div class="foot-contact" style="top:27px"><svg width="20" height="14" viewBox="0 0 20 14"><rect x="1" y="1" width="18" height="12" fill="none" stroke="#fff" stroke-width="1.5"/><path d="M1 1 10 8 19 1" fill="none" stroke="#fff" stroke-width="1.5"/></svg>info@rtharlow.com</div>
  <div class="foot-contact" style="top:64px;left:438px;font-weight:500"><svg width="17" height="17" viewBox="0 0 24 24"><path fill="#fff" d="M6.6 10.8a15 15 0 0 0 6.6 6.6l2.2-2.2a1 1 0 0 1 1-.25 11.4 11.4 0 0 0 3.6.57 1 1 0 0 1 1 1V20a1 1 0 0 1-1 1A17 17 0 0 1 3 4a1 1 0 0 1 1-1h3.5a1 1 0 0 1 1 1c0 1.25.2 2.45.57 3.57a1 1 0 0 1-.25 1z"/></svg>07700900417</div>
  <div class="foot-divider" style="left:663px"></div>
  <div class="foot-brand"><i class="mark"></i>R.T.Harlow</div>
</footer>
<div class="foot-bar">
  <span class="copy">Copyright 2018 RTHarlow Construction LTD. All rights reserved.</span>
  <div class="social" aria-label="Social media links"><span></span><span></span><span></span></div>
</div>

</body>
</html>
```